Awesome Business Card Design needed!

Hey there.
I'm looking for a simple but awesome business card design.
Type of company: Online advertisement agency
(please don't use the typical business people or statistics images on the card)
The front has to display the business name
and possibly some sort of logo ( perhaps something with the two M's of the biz name )
And the back of the card should say:
Name
Phone
Email
Let your imagination flow.
here are some designs that I like and that you can use as inspiration.
Simple but Awesome
http://images.pixelvane.example/designs/55128_877673_43091_thumbnail.jpg
http://images.pixelvane.example/designs/37714_747642_40106_image.jpg
http://images.pixelvane.example/designs/55128_877673_43091_image.jpg
http://images.pixelvane.example/designs/51321_781878_43091_image.jpg
http://images.pixelvane.example/designs/33378_399063_15912_image.jpg
http://images.pixelvane.example/designs/2337_271604_9495_image.jpg
good luck

```html
<!DOCTYPE html>
<html lang="en">
<head>
<meta charset="utf-8">
<title>Corven Media – Business Cards</title>
<link rel="stylesheet" href="https://fonts.googleapis.com/css2?family=Libre+Bodoni:wght@700&family=Open+Sans:wght@400&display=swap">
<style>
  :root {
    --bg-top: #1b1c1d;
    --bg-bottom: #f2f2f2;
    --card-black: #060708;
    --card-dark: #0d0f10;
    --glow: #5c6267;
    --tile-light: #c9cccd;
    --tile-dark: #1a1c1d;
    --text-white: #ffffff;
    --text-silver: #d9dcde;
    --mark-dark: #0a0b0c;
  }
  * { margin: 0; padding: 0; box-sizing: border-box; }
  html, body { width: 1200px; height: 1200px; overflow: hidden; }
  body {
    background: linear-gradient(180deg, var(--bg-top) 0%, #6b6d6f 45%, var(--bg-bottom) 100%);
    position: relative;
    font-family: "Open Sans", Arial, sans-serif;
  }
  .card {
    position: absolute;
    overflow: hidden;
    background: var(--card-black);
    box-shadow: 0 14px 30px rgba(0,0,0,0.45);
  }
  .card svg.card-art { position: absolute; inset: 0; width: 100%; height: 100%; }

  /* Back card: contact details */
  .card-back { left: 112px; top: 122px; width: 568px; height: 322px; }
  .contact {
    position: absolute;
    left: 220px; top: 168px; width: 240px;
    text-align: center;
    color: var(--text-white);
    font-size: 17px;
    line-height: 25px;
  }

  /* Front card: company */
  .card-front { left: 397px; top: 480px; width: 688px; height: 428px; }
  .wordmark {
    position: absolute;
    right: 40px; top: 52px;
    text-align: center;
  }
  .wordmark-name {
    font-family: "Libre Bodoni", "Bodoni Moda", Georgia, serif;
    font-weight: 700;
    font-size: 30px;
    color: var(--text-silver);
    line-height: 1;
  }
  .wordmark-tagline {
    font-family: "Libre Bodoni", Georgia, serif;
    font-weight: 700;
    font-size: 12.5px;
    color: var(--text-silver);
    margin-top: 6px;
  }
  .front-name {
    position: absolute;
    left: 40px; bottom: 30px;
    font-family: "Libre Bodoni", Georgia, serif;
    font-weight: 700;
    font-size: 48px;
    color: var(--mark-dark);
    line-height: 1;
  }
</style>
</head>
<body>

  <section class="card card-back" aria-label="Back of business card">
    <svg class="card-art" viewBox="0 0 568 322" preserveAspectRatio="none">
      <defs>
        <radialGradient id="backTiles" cx="0.55" cy="0.35" r="0.7">
          <stop offset="0" stop-color="var(--tile-light)"/>
          <stop offset="0.5" stop-color="#6a6e70"/>
          <stop offset="1" stop-color="var(--tile-dark)"/>
        </radialGradient>
      </defs>
      <path role="img" aria-label="Lit tiled surface texture"
            d="M0 0 L318 0 C300 70 230 140 0 152 Z" fill="url(#backTiles)"/>
      <path d="M318 0 C300 70 230 140 0 152" fill="none" stroke="#8d9295" stroke-width="2" opacity="0.6"/>
    </svg>
    <div class="contact">
      <p class="contact-name">Daniel Harrow</p>
      <p class="contact-phone">phone: 00385 1 555010</p>
      <p class="contact-email">daniel@corvenmedia.example</p>
    </div>
  </section>

  <section class="card card-front" aria-label="Front of business card">
    <svg class="card-art" viewBox="0 0 688 428" preserveAspectRatio="none">
      <defs>
        <radialGradient id="frontTiles" cx="0.35" cy="0.85" r="0.55">
          <stop offset="0" stop-color="var(--tile-light)"/>
          <stop offset="0.45" stop-color="#5e6264"/>
          <stop offset="1" stop-color="var(--tile-dark)"/>
        </radialGradient>
        <radialGradient id="darkSweep" cx="0.85" cy="0.08" r="0.75">
          <stop offset="0" stop-color="var(--glow)"/>
          <stop offset="0.45" stop-color="#1c1f21"/>
          <stop offset="1" stop-color="var(--card-dark)"/>
        </radialGradient>
      </defs>
      <rect role="img" aria-label="Lit tiled surface texture"
            width="688" height="428" fill="url(#frontTiles)"/>
      <path d="M122 0 C150 180 330 345 560 345 L688 342 L688 0 Z" fill="url(#darkSweep)"/>
    </svg>
    <div class="wordmark">
      <p class="wordmark-name">Corven Media</p>
      <p class="wordmark-tagline">online advertisement agency</p>
    </div>
    <p class="front-name">Corven</p>
  </section>

</body>
</html>
```